We are wanting a designer to design an ebook on Residential Property in Australia. This ebook is a quarterly report and covers 5 major capital cities in Australia. This is the first quarterly report for the year - another 3 are needed to be created. If you are chosen as our designer please expect ongoing work which is well rewarded.

To begin with:

We will only need you to design a few pages so we can see your style. Then if you are chosen we will get you to do the whole thing.

Can you please design the title page, page 5 and the Adelaide section(page 6 & 7) of the The Suburban Dwelling Forecast - Seasonal Capital Briefing - Q1 2014 document attached.

The ebook brief:

You will need to create 2 graphs to include in the ebook from the data I give to you for each capital city (one graph for houses and one graph for units).

We already have a style of ebook in mind from a previous ebook our in-office designer has created for our company. You will need to keep with the logo/style/colours/fonts etc. We are looking for a designer based in Australia.

Sources and content:

Below I have shared a dropbox folder with you. It contains the first ebook our designer has created for you to view the style,logo etc - YieldHaven-Property-ebook. The folder also contains the source files for the logo.

https://www.filecrate-share.com/sh/k4p2xq7vb9rm3d/BXQ581zt/

The Suburban Dwelling Forecast - Seasonal Capital Briefing - Q1 2014 document attached is the content we need made into the ebook.

Each page has been set out with the content needed for that page. Each capital city content spreads out over two pages with a graph on each. I have highlighted in red the data needed to create each of the graphs. The graph style must look like the Sector Horizon image in the shared dropbox folder.

You will also need to redesign the graph on page 5. You may do this how you like as long as it keeps in the style of the ebook. We will also need the source files on this ebook.

```html
<!DOCTYPE html>
<html lang="en">
<head>
<meta charset="utf-8">
<title>Positive Growth – YieldHaven</title>
<link href="https://fonts.googleapis.com/css2?family=Source+Sans+3:wght@300;400;600;700&display=swap" rel="stylesheet">
<style>
  :root {
    --red: #c8202f;
    --red-dark: #9c1520;
    --red-deep: #7e0f18;
    --beige: #c9b99b;
    --blue: #1f5b8c;
    --ink: #2b2b2b;
    --grid: #bdbdbd;
    --shade: #ececec;
    --paper: #ffffff;
    --wood: #8a5a3a;
    --cream: #e9dfd2;
  }
  * { margin: 0; padding: 0; box-sizing: border-box; }
  html, body { width: 848px; height: 1200px; overflow: hidden; background: var(--paper); }
  body { font-family: "Source Sans 3", "Myriad Pro", Arial, sans-serif; color: var(--ink); }
  .page { position: relative; width: 848px; height: 1200px; overflow: hidden; }

  .band-top {
    position: absolute; left: 0; top: 0; width: 848px; height: 121px;
    background: linear-gradient(135deg, var(--red-deep) 0%, var(--red) 45%, var(--red-dark) 100%);
  }
  .region-badge {
    position: absolute; right: 24px; top: 40px; width: 54px; height: 50px;
    background: rgba(255,255,255,0.9); border-radius: 6px;
  }
  .hero-photo {
    position: absolute; left: 0; top: 121px; width: 848px; height: 338px;
    background: linear-gradient(100deg, var(--cream) 0%, #b89479 30%, var(--wood) 55%, #c8a98a 75%, #6b3f27 100%);
  }
  .band-bottom {
    position: absolute; left: 0; top: 459px; width: 848px; height: 61px;
    background: linear-gradient(135deg, var(--red-dark) 0%, var(--red) 55%, var(--red-deep) 100%);
  }

  .headline {
    position: absolute; left: 45px; top: 553px;
    font-size: 33px; font-weight: 700; color: var(--red); letter-spacing: 0.2px; line-height: 1;
  }
  .subhead {
    position: absolute; left: 45px; top: 593px;
    font-size: 29px; font-weight: 300; color: var(--blue); line-height: 1;
  }
  .body-copy { position: absolute; left: 45px; top: 651px; width: 762px; }
  .body-copy p { font-size: 14.6px; line-height: 20.5px; margin-bottom: 20px; }

  .chart { position: absolute; left: 190px; top: 880px; width: 440px; height: 285px; }

  .brand-mark {
    position: absolute; left: 716px; top: 1078px; width: 112px;
    display: flex; flex-direction: column; align-items: center; gap: 8px;
  }
  .brand-square { width: 58px; height: 58px; background: var(--red); }
  .brand-name { font-size: 18px; font-weight: 700; color: var(--red); }
</style>
</head>
<body>
<main class="page">
  <div class="band-top" role="img" aria-label="Red banner with a fine white geometric line pattern">
    <div class="region-badge" role="img" aria-label="Small white map outline of Australia"></div>
  </div>
  <div class="hero-photo" role="img" aria-label="Photo of a modern open-plan home interior with kitchen, timber floors, lounge and dining room"></div>
  <div class="band-bottom" role="img" aria-label="Red banner with a fine white geometric line pattern"></div>

  <h1 class="headline">POSITIVE GROWTH</h1>
  <h2 class="subhead">More million dollar suburbs than ever before</h2>

  <section class="body-copy">
    <p>A positive indicator of a strong property market is the number of suburbs which record a million dollar median price range. This is becoming a common feature in property markets across most Australian capital cities.</p>
    <p>According to recent statistics from Valuemetrics, the residential property market is booming with million dollar suburbs. Australia currently has 279 suburbs where the house price median is one million or more, and 23 suburbs where the average unit price is one million or above.</p>
    <p>In the housing market, Sydney currently leads the nation with 181 recorded million dollar suburbs. This is followed by Melbourne with 51, Perth with 43, Brisbane with 13, and Adelaide with 8. (Source: Valuemetrics)</p>
  </section>

  <svg class="chart" viewBox="0 0 440 285" font-family="Source Sans 3, Arial, sans-serif" aria-label="Capital City Median Property Values chart">
    <text x="235" y="10" text-anchor="middle" font-size="10" font-weight="700" fill="#222">Capital City Median Property Values</text>
    <text x="235" y="22" text-anchor="middle" font-size="10" font-weight="700" fill="#222">(Houses and Units)</text>
    <!-- shaded smaller-centre zone -->
    <rect x="290" y="30" width="140" height="190" fill="var(--shade)"/>
    <g stroke="var(--grid)" stroke-width="0.7">
      <line x1="58" x2="430" y1="39.4" y2="39.4"/>
      <line x1="58" x2="430" y1="62.8" y2="62.8"/>
      <line x1="58" x2="430" y1="86.1" y2="86.1"/>
      <line x1="58" x2="430" y1="109.5" y2="109.5"/>
      <line x1="58" x2="430" y1="132.9" y2="132.9"/>
      <line x1="58" x2="430" y1="156.3" y2="156.3"/>
      <line x1="58" x2="430" y1="179.6" y2="179.6"/>
      <line x1="58" x2="430" y1="203" y2="203"/>
    </g>
    <g font-size="7" fill="#222" text-anchor="end">
      <text x="54" y="42">$800,000</text>
      <text x="54" y="65">$700,000</text>
      <text x="54" y="89">$600,000</text>
      <text x="54" y="112">$500,000</text>
      <text x="54" y="135">$400,000</text>
      <text x="54" y="159">$300,000</text>
      <text x="54" y="182">$200,000</text>
      <text x="54" y="206">$100,000</text>
    </g>
    <!-- bars: base y=226.4, 0.2338px per $1k -->
    <g fill="var(--red)">
      <rect x="66" y="132.5" width="16" height="93.9"/>
      <rect x="112" y="119.8" width="16" height="106.6"/>
      <rect x="158" y="83.8" width="16" height="142.6"/>
      <rect x="204" y="102.8" width="16" height="123.6"/>
      <rect x="250" y="45.9" width="16" height="180.5"/>
      <rect x="297" y="103.3" width="16" height="123.1"/>
      <rect x="343" y="88.2" width="16" height="138.2"/>
      <rect x="389" y="138.4" width="16" height="88"/>
    </g>
    <g fill="var(--beige)">
      <rect x="84" y="155.1" width="16" height="71.3"/>
      <rect x="130" y="143.2" width="16" height="83.2"/>
      <rect x="176" y="121.5" width="16" height="104.9"/>
      <rect x="222" y="120.2" width="16" height="106.2"/>
      <rect x="268" y="100.8" width="16" height="125.6"/>
      <rect x="315" y="130.9" width="16" height="95.5"/>
      <rect x="361" y="124.1" width="16" height="102.3"/>
      <rect x="407" y="167.5" width="16" height="58.9"/>
    </g>
    <line x1="58" x2="430" y1="226.4" y2="226.4" stroke="#888" stroke-width="0.8"/>
    <g font-size="4.5" fill="#222" text-anchor="middle">
      <text x="74" y="130">401,500</text><text x="92" y="153">305,000</text>
      <text x="120" y="117">456,000</text><text x="138" y="141">356,000</text>
      <text x="166" y="81">610,000</text><text x="184" y="119">448,500</text>
      <text x="212" y="100">528,500</text><text x="230" y="118">454,000</text>
      <text x="258" y="43">772,000</text><text x="276" y="98">537,000</text>
      <text x="305" y="101">526,500</text><text x="323" y="128">408,500</text>
      <text x="351" y="86">591,000</text><text x="369" y="122">437,400</text>
      <text x="397" y="136">376,500</text><text x="415" y="165">252,000</text>
    </g>
    <g font-size="7.5" fill="#222" text-anchor="middle">
      <text x="83" y="237">Adelaide</text>
      <text x="129" y="237">Brisbane</text>
      <text x="175" y="237">Melbourne</text>
      <text x="221" y="237">Perth</text>
      <text x="267" y="237">Sydney</text>
      <text x="314" y="237">Canberra</text>
      <text x="360" y="237">Darwin</text>
      <text x="406" y="237">Hobart</text>
    </g>
    <g font-size="7" fill="var(--blue)" text-anchor="middle">
      <text x="174" y="249">Population centres greater than 1 million</text>
      <text x="360" y="249">Population centres under 360,000</text>
    </g>
    <g font-size="5" fill="#333">
      <text x="10" y="257">Graph 1.0</text>
      <text x="10" y="264">Source: Valuemetrics, Keelstone Property Research</text>
    </g>
    <g font-size="6.5" fill="#222">
      <text x="175" y="262">HOUSES</text>
      <rect x="205" y="256" width="28" height="8" fill="var(--red)"/>
      <text x="246" y="262">UNITS</text>
      <rect x="270" y="256" width="28" height="8" fill="var(--beige)"/>
    </g>
    <text x="330" y="263" font-size="7" font-weight="700" fill="#e0702a">Keelstone</text>
  </svg>

  <div class="brand-mark">
    <div class="brand-square"></div>
    <span class="brand-name">YieldHaven</span>
  </div>
</main>
</body>
</html>
```